Design Health Food E-Book for Small Business Using Provided Content

My business is looking for a designer to design and create an e-book PDF with recipes and images.

The required work will be:

Designing layout of e-book based on provided (below) e-book sample.

Adding supplied recipes and images into a PDF format

Iterating PDF until the work has reached satisfactory requirements

The outcome will be:

1 PDF document (roughly 10-15 pages) created using supplied recipes and images

This recipe e-book by Tessa Morrow should serve as a strong piece of inspiration.

https://brightplatekitchen.example.com/item/7c41d2e9a0f3b615397e8b04

The full content of the e-book, including photos and copy, can be found here:

https://files.example-share.net/sh/kqe915tz47w203x/BBxRnugwXMpoHeTvQjKsZWy4Fb?dl=0

Please arrange for a skype conversation if further clarification of e-book output and/or design are necessary.

Email: rowlet819@mailbrook.net

Industry/Entity Type

Health And Wellness

Font styles to use
Other font styles liked:
• Designer Choice

Requirements
Must have
• Book-like appearance (as in actually looks like a recipe book as opposed to a flyer, photo collection etc.
• Flawless page-linking (from contents page and to external sources) and no errors in text (unless we put a typo in!)
• Cute extra graphics (as per supplied Tessa Morrow book)
Nice to have
• Designer interested in health food
• Experience in e-book design
Should not have
• Typos
• Errors in text linking

```html
<!DOCTYPE html>
<html lang="en">
<head>
<meta charset="utf-8">
<title>Monday – Choc-Orange Buckwheat Granola</title>
<link href="https://fonts.googleapis.com/css2?family=Sacramento&family=Open+Sans:ital,wght@0,400;0,700;1,400&family=Tinos:wght@400&display=swap" rel="stylesheet">
<style>
  :root {
    --paper: #ffffff;
    --ink: #1c1c1c;
    --body: #333333;
    --peach: #e8c8b4;
    --peach-soft: #f1dccf;
    --rule: #9a9a9a;
    --photo-marble: #d9dde3;
    --photo-bowl: #b86a4a;
  }
  * { box-sizing: border-box; margin: 0; padding: 0; }
  html, body { width: 1200px; height: 849px; overflow: hidden; background: var(--paper); }
  .spread { position: relative; width: 1200px; height: 849px; background: var(--paper); }

  .hero-photo {
    position: absolute; left: 0; top: 0; width: 600px; height: 849px;
    background: radial-gradient(circle at 290px 440px, var(--photo-bowl) 0, #c98a5e 150px, #e6e1dc 255px, var(--photo-marble) 265px, #cfd4db 600px);
  }
  .slice-mark { position: absolute; border-radius: 50%; background: var(--peach-soft); opacity: .75; }

  .page { position: absolute; left: 600px; top: 0; width: 600px; height: 849px; }
  .day-label {
    position: absolute; top: 14px; left: 0; width: 100%; text-align: center; padding-left: 0;
    font-family: "Sacramento", cursive; font-size: 58px; color: var(--peach); line-height: 1;
    padding-right: 0; transform: translateX(0);
  }
  .recipe-title {
    position: absolute; top: 96px; left: 0; width: 100%; text-align: center;
    font-family: "Tinos", "Times New Roman", serif; font-weight: 400; font-size: 25px; color: var(--ink);
  }
  .recipe-intro {
    position: absolute; top: 142px; left: 20px; width: 560px; text-align: center;
    font-family: "Open Sans", sans-serif; font-size: 14.2px; line-height: 24px; color: var(--body);
  }
  .recipe-meta {
    position: absolute; top: 204px; left: 0; width: 100%; text-align: center;
    font-family: "Open Sans", sans-serif; font-style: italic; font-size: 14px; line-height: 24px; color: var(--body);
  }
  .section-heading {
    font-family: "Tinos", "Times New Roman", serif; font-weight: 400; font-size: 16.5px;
    text-decoration: underline; text-underline-offset: 3px; color: var(--ink);
  }
  .ingredients { position: absolute; top: 294px; left: 32px; width: 230px; }
  .ingredients ul { list-style: none; margin-top: 24px; }
  .ingredients li {
    font-family: "Open Sans", sans-serif; font-style: italic; font-size: 12.3px; line-height: 18px;
    color: var(--body); margin-bottom: 6px; padding-left: 10px; text-indent: -10px;
  }
  .column-rule { position: absolute; left: 265px; top: 292px; width: 1px; height: 506px; background: var(--rule); }
  .method { position: absolute; top: 294px; left: 288px; width: 292px; }
  .method ol { list-style: none; margin-top: 30px; counter-reset: step; }
  .method li {
    position: relative; padding-left: 18px; margin-bottom: 6px; counter-increment: step;
    font-family: "Open Sans", sans-serif; font-size: 10.4px; line-height: 18.4px; color: var(--body);
  }
  .method li::before { content: counter(step) "."; position: absolute; left: 0; top: 0; }
  .method a { color: var(--ink); font-weight: 700; text-decoration: underline; }
</style>
</head>
<body>
<div class="spread">
  <div class="hero-photo" role="img" aria-label="Overhead photo of a bowl of chocolate buckwheat granola with coconut flakes, hazelnuts, banana, mandarin, raspberries and passionfruit, with a wooden spoon, on white marble"></div>
  <div class="slice-mark" role="img" aria-label="Hand-drawn orange slice decoration" style="left:-12px;top:-20px;width:100px;height:100px;"></div>
  <div class="slice-mark" role="img" aria-label="Hand-drawn orange slice decoration" style="left:118px;top:-18px;width:98px;height:82px;"></div>
  <div class="slice-mark" role="img" aria-label="Hand-drawn orange slice decoration" style="left:93px;top:86px;width:74px;height:70px;"></div>

  <section class="page">
    <div class="day-label">Monday</div>
    <h1 class="recipe-title">Choc-Orange Buckwheat Granola</h1>
    <p class="recipe-intro">A crunchy, chocolatey granola with a hint of orange. This recipe will make a big batch which you can enjoy for many breakfasts to come!</p>
    <p class="recipe-meta">Makes 1 large jar (4-5 serves)<br>GF, DF, Vegan, RSF</p>

    <div class="ingredients">
      <h2 class="section-heading">YOU WILL NEED:</h2>
      <ul>
        <li>Juice and rind of one large orange</li>
        <li>2 Tbsp. tahini</li>
        <li>1/4 cup water</li>
        <li>1/3 cup maple syrup (or sweetener of your choice)</li>
        <li>1/2 tsp salt</li>
        <li>2 Tbsp. cacao powder</li>
        <li>1 Tbsp. mesquite powder (optional - adds a delicious caramel flavour)</li>
        <li>1/2 cup hazelnuts</li>
        <li>1/3 cup cacao nibs</li>
        <li>2 cups raw buckwheat</li>
        <li>1/2 cup coconut flakes</li>
      </ul>
    </div>

    <div class="column-rule"></div>

    <div class="method">
      <h2 class="section-heading">HOW TO:</h2>
      <ol>
        <li>Preheat oven to 160°C (320°F)</li>
        <li>Whisk orange juice, tahini, water and maple syrup together in a small bowl</li>
        <li>Add orange rind, cacao powder, salt, and mesquite (if using) and stir well to remove any lumps</li>
        <li>In a large bowl, mix hazelnuts, cacao nibs and buck wheat. Pour over wet ingredients and stir well</li>
        <li>Line a baking tray with baking paper and spoon out the granola mix. Spread evenly around the tray using the back of a spoon</li>
        <li>The granola will take around 35- 40 minutes total to bake. After the first 15-20 minutes of initial baking, take the tray out of the oven and use a spatula to flip some of the granola over and break up large pieces so that the granola can bake evenly. Return to the oven for another 20-25 minutes until browned and crunchy but not burned</li>
        <li>Remove from oven and allow to cool completely (necessary for the granola to become perfectly crunchy). Stir through the coconut flakes and serve with fresh fruit and <a href="#almond-milk">almond milk</a>. Store leftovers in an air tight jar for up to two weeks. Happy munching!</li>
      </ol>
    </div>

    <div class="slice-mark" role="img" aria-label="Hand-drawn orange slice decoration" style="left:-10px;top:656px;width:104px;height:132px;"></div>
    <div class="slice-mark" role="img" aria-label="Hand-drawn orange slice decoration" style="left:118px;top:704px;width:76px;height:72px;"></div>
    <div class="slice-mark" role="img" aria-label="Hand-drawn orange slice decoration" style="left:66px;top:790px;width:104px;height:80px;"></div>
  </section>
</div>
</body>
</html>
```